Meridel Capra SA Business Cards

Dear all,
Thank you for reading my brief and project. My company is doing doing advisory in real estate and to comapnies + real estates services as asset management, brokerage, development etc.
I would like to get a business card for my company which is clear, professionnal and serious.
Please have a look to the attachement to see the logos of the company

Industry/Entity Type

Real Estate

Contact Information for Business Card

I would like to have in the business card the following
Principal side:
- Logo of the company (or Monogram)
- First and Last Name (Paulo Vestrand)
- Mobile number
- email address

Second side:
- Address (Chemin des Orvets 17, 1226 Thônex - Switzerland)
- website (www.meridelcapra.ch)

Requirements
Must have
• Refer to the typeface and logo colors

```html
<!DOCTYPE html>
<html lang="en">
<head>
<meta charset="utf-8">
<title>Meridel Capra SA – Business Cards</title>
<link rel="stylesheet" href="https://fonts.googleapis.com/css2?family=Lato:wght@400;700;900&display=swap">
<style>
  :root {
    --bg: #dcdcdd;
    --slate: #3a4657;
    --blue: #0a75c6;
    --white: #ffffff;
    --ink: #3a4657;
  }
  * { box-sizing: border-box; margin: 0; padding: 0; }
  html, body {
    width: 1200px; height: 900px; overflow: hidden;
    background: var(--bg);
    font-family: "Lato", Arial, sans-serif;
  }
  .canvas { position: relative; width: 1200px; height: 900px; }
  .card {
    position: absolute;
    width: 560px; height: 340px;
    border-radius: 26px;
    overflow: hidden;
    box-shadow: 0 10px 26px rgba(0,0,0,0.18);
  }

  .brand-row {
    position: absolute;
    display: flex; align-items: center; gap: 24px;
  }
  .brand-square { width: 52px; height: 52px; background: var(--blue); flex: none; }
  .divider { width: 1.5px; height: 76px; background: var(--blue); flex: none; }
  .brand-name {
    font-weight: 700; font-size: 29px; letter-spacing: 1px;
    text-transform: uppercase; white-space: nowrap;
  }

  /* Back side */
  .card-back { left: 80px; top: 90px; background: var(--slate); }
  .card-back .brand-row { left: 70px; top: 70px; }
  .card-back .brand-name { color: var(--blue); }
  .card-back .address {
    position: absolute; left: 172px; top: 180px;
    color: var(--white); font-size: 17px; line-height: 1.35;
  }
  .card-back .web-band {
    position: absolute; left: 0; right: 0; bottom: 0; height: 62px;
    background: var(--blue);
    display: flex; align-items: center; justify-content: center;
  }
  .web-band .website {
    color: var(--white); font-size: 16px; letter-spacing: 1px; text-transform: uppercase;
  }

  /* Front side */
  .card-front { left: 560px; top: 470px; background: var(--white); }
  .card-front .brand-row { left: 40px; top: 58px; }
  .card-front .brand-name { color: var(--ink); }
  .card-front .person {
    position: absolute; left: 40px; top: 194px;
    font-size: 24px; letter-spacing: 0.5px; text-transform: uppercase;
  }
  .person .first { font-weight: 900; color: var(--ink); }
  .person .last { font-weight: 400; color: var(--blue); }
  .contacts {
    position: absolute; left: 40px; top: 238px;
    list-style: none; color: var(--ink); font-size: 19px;
  }
  .contacts li { display: flex; align-items: center; gap: 8px; margin-bottom: 6px; }
  .contacts svg { width: 18px; height: 18px; fill: var(--blue); }
</style>
</head>
<body>
<div class="canvas">

  <section class="card card-back" aria-label="Business card, back side">
    <div class="brand-row">
      <span class="brand-square" aria-hidden="true"></span>
      <span class="divider"></span>
      <span class="brand-name">Meridel Capra</span>
    </div>
    <p class="address">Chemin des Orvets 17, 1226<br>Thônex - Switzerland</p>
    <div class="web-band">
      <span class="website">www.meridelcapra.ch</span>
    </div>
  </section>

  <section class="card card-front" aria-label="Business card, front side">
    <div class="brand-row">
      <span class="brand-square" aria-hidden="true"></span>
      <span class="divider"></span>
      <span class="brand-name">Meridel Capra</span>
    </div>
    <p class="person"><span class="first">Paulo</span> <span class="last">Vestrand</span></p>
    <ul class="contacts">
      <li>
        <svg viewBox="0 0 24 24" aria-hidden="true"><path d="M6.6 10.8a15 15 0 0 0 6.6 6.6l2.2-2.2a1 1 0 0 1 1-.25 11.4 11.4 0 0 0 3.6.57 1 1 0 0 1 1 1V20a1 1 0 0 1-1 1A17 17 0 0 1 3 4a1 1 0 0 1 1-1h3.5a1 1 0 0 1 1 1c0 1.25.2 2.45.57 3.6a1 1 0 0 1-.25 1z"/></svg>
        <span>044-555 018 274</span>
      </li>
      <li>
        <svg viewBox="0 0 24 24" aria-hidden="true"><path d="M2 5h20v14H2z"/><path d="M3.5 6.8 12 13.2l8.5-6.4" fill="none" stroke="#fff" stroke-width="1.5"/></svg>
        <span>info@meridelcapra.ch</span>
      </li>
    </ul>
  </section>

</div>
</body>
</html>
```